A Writer With A Website (Writes action/mysteries with a touch of romance thrown in)

I need a website. I am an unpublished writer. I own a domain and tried a bit to design one in Wordpress. I would like to be able to change out pictures, blog, and receive email. My fav color is orange (but not necessary in website) I like the font "Hello Stockholm" Probably 4 or five different pages. Attached is a poor scan of a business card.
Updates

Had a recent death in the family, my inspiration to get the site designed and also the reason I may need a few days.

I write books action mysteries. So far all take place in Wyoming. I realize there was not much info given. Pages: Home, Looking for representation, recommended reading and other things I like, Marlena (a page dedicated to my daughter who just passed away), and other useful links. Probably shorter ways to say those, but you get the idea.

Thanks for the designs submitted. I know I gave very little direction. There are a few authors who write in Wyoming who are popular, TR Hale, Dwight Pellman (Ashcombe Series) I would argue that the main character in any of their books is Wyoming, or the West. No cliches. Cowboy hats, horses, not so good. For those outside the US, maybe do a serch on Wyoming and look at the pictures. I have photo's for possible use in my design, will post them tonight. Thanks all. -j-

I am not sure how much info gets added, how much the designer does and how I fill in the "blanks". Here is partial text for the "Marlena" page: Over the years, our daughters’ friends overlapped one another and two or three became like daughters to Velma and me. Some even became our friends as they grew into adulthood. One had a father who tried to committed suicide multiple times. After one attempt she asked him, “why?” He said, “I am glad you can’t understand why, only someone who can travel to that dark a place can understand why”. He was eventually successful. She shared that story with us on August 14th when our daughter Marlena found that dark place in herself and took her life. We found a suicide note, then her body, then everything went into a fog. An hour or so later, my wife and I stood on the front lawn after the police interviews and watched as the corner slide a covered corpse into the white SUV with darkened windows. We stood there as the rain began to fall, and the sky sobbed with us. As they closed the back of the coroner’s Wayfarer, the rain fell harder and harder and a fireman guided us back into the house that will never be the same for us.

Target Market(s)

Currently trying to get an agent, this is to look like I have followers.

Number of Pages Required

5+ page

Font styles to use
Serif

Colors
f68e4e

Requirements
Nice to have
• I like orange (more of a burnt orange color) I am a big fan of Bertrand Ollesko. A "feel" like that might be nice. I am from Wyoming, That rugged western culture shows up in all my writing.
Should not have
• Western Cliche,

```html
<!DOCTYPE html>
<html lang="en">
<head>
<meta charset="utf-8">
<title>R L Varden — Author</title>
<link href="https://fonts.googleapis.com/css2?family=Rubik:wght@400;500;700&family=Heebo:wght@400;500&family=Mrs+Saint+Delafield&family=Yellowtail&display=swap" rel="stylesheet">
<style>
  :root {
    --paper: #d5ba8b;
    --paper-dark: #c9ad7d;
    --burnt: #ab4305;
    --flame: #ef5628;
    --ink: #111111;
    --grey-text: #6a6a6a;
    --white: #ffffff;
  }
  * { box-sizing: border-box; margin: 0; padding: 0; }
  html, body { width: 1200px; height: 1000px; overflow: hidden; background: var(--white); }
  body { position: relative; font-family: "Heebo", Arial, sans-serif; color: var(--ink); }

  .paper { position: absolute; background: radial-gradient(ellipse at 30% 40%, var(--paper) 0%, var(--paper-dark) 100%); }
  .paper--top { left: 0; top: 0; width: 725px; height: 613px; }
  .paper--bottom { left: 0; top: 787px; width: 1200px; height: 185px; }

  .brand { position: absolute; left: 72px; top: 46px; }
  .brand__name { font-family: "Rubik", Arial, sans-serif; font-weight: 500; font-size: 36px; color: var(--flame); line-height: 52px; letter-spacing: 1px; white-space: nowrap; }
  .brand__site { margin-left: 23px; margin-top: 10px; font-size: 13px; line-height: 16px; white-space: nowrap; }

  .social { position: absolute; top: 40px; right: 527px; display: flex; gap: 12px; }
  .social__item { font-family: "Rubik", Arial, sans-serif; font-size: 11px; font-weight: 500; display: flex; align-items: center; gap: 4px; }
  .social__dot { width: 9px; height: 9px; background: var(--ink); }

  .nav { position: absolute; left: 349px; top: 86px; display: flex; align-items: center; font-family: "Rubik", Arial, sans-serif; font-weight: 500; font-size: 13px; white-space: nowrap; }
  .nav__home { width: 24px; height: 22px; margin-right: 25px; }
  .nav__link { margin-right: 25px; }

  .author-photo { position: absolute; z-index: 2; left: 66px; top: 162px; width: 300px; height: 625px; background: linear-gradient(170deg, #5c5346 0%, #8d8168 40%, #6b6150 100%); }
  .owl-art { position: absolute; z-index: 2; left: 366px; top: 548px; width: 161px; height: 239px; background: radial-gradient(ellipse at 50% 45%, #7b5a36 0%, #4e3620 70%, #3a2717 100%); border-radius: 60px 70px 0 0; }

  .intro { position: absolute; left: 400px; top: 179px; width: 273px; font-size: 12.5px; line-height: 16.8px; text-align: justify; hyphens: auto; }
  .intro p { margin-bottom: 16.8px; }

  .memorial-title { position: absolute; left: 782px; top: 42px; width: 320px; height: 110px; font-weight: 400; }
  .memorial-title__lead { position: absolute; left: 0; top: 12px; font-family: "Mrs Saint Delafield", cursive; font-size: 30px; line-height: 34px; transform: rotate(-8deg); white-space: nowrap; }
  .memorial-title__name { position: absolute; left: 140px; top: 4px; font-family: "Yellowtail", cursive; font-size: 64px; line-height: 96px; color: var(--flame); white-space: nowrap; }

  .memorial-text { position: absolute; left: 786px; top: 179px; width: 332px; font-size: 12.5px; line-height: 16.8px; color: var(--grey-text); text-align: justify; hyphens: auto; }
  .memorial-text p { margin-bottom: 16.8px; }

  .newsletter { position: absolute; z-index: 1; left: 1px; top: 613px; width: 1199px; height: 174px; background: var(--burnt); }
  .newsletter__title { position: absolute; left: 555px; top: 58px; font-family: "Rubik", Arial, sans-serif; font-weight: 500; font-size: 21px; line-height: 29px; color: var(--white); white-space: nowrap; }
  .newsletter__icon { width: 46px; height: 30px; vertical-align: -4px; margin-left: 4px; }
  .newsletter__form { position: absolute; left: 772px; top: 70px; display: flex; }
  .newsletter__input { width: 215px; height: 41px; border: 0; background: var(--white); }
  .newsletter__button { width: 130px; height: 41px; border: 0; background: #000; color: var(--white); font-family: "Rubik", Arial, sans-serif; font-weight: 500; font-size: 15px; }

  .recommend-title { position: absolute; left: 66px; top: 830px; font-family: "Rubik", Arial, sans-serif; font-weight: 500; font-size: 22px; line-height: 29px; color: var(--burnt); white-space: nowrap; }
  .recommend-title__icon { width: 42px; height: 42px; vertical-align: -6px; margin-left: 6px; }

  .book { position: absolute; top: 817px; display: flex; align-items: center; }
  .book__cover { width: 92px; height: 123px; background: linear-gradient(160deg, #c9d8e8 0%, #6a86b1 45%, #354d78 100%); }
  .book__title { margin-left: 14px; font-family: "Rubik", Arial, sans-serif; font-size: 14px; line-height: 16px; }
  .book--one { left: 368px; } .book--two { left: 620px; } .book--three { left: 872px; }

  .footer { position: absolute; left: 0; top: 972px; width: 1200px; height: 28px; text-align: center; font-size: 12.5px; line-height: 28px; color: #555; }
</style>
</head>
<body>
  <div class="paper paper--top"></div>
  <div class="paper paper--bottom"></div>

  <header>
    <div class="brand">
      <div class="brand__name">R L Varden</div>
      <div class="brand__site">InkAndPlains.com</div>
    </div>
    <div class="social">
      <span class="social__item"><span class="social__dot"></span>Flit</span>
      <span class="social__item"><span class="social__dot"></span>Pagebook</span>
    </div>
    <nav class="nav">
      <svg class="nav__home" viewBox="0 0 24 22" aria-label="Home"><path d="M12 1 L1 11 H4 V21 H10 V14 H14 V21 H20 V11 H23 Z" fill="#111"/></svg>
      <span class="nav__link">About Me</span>
      <span class="nav__link">Books</span>
      <span class="nav__link">Blog</span>
      <span class="nav__link">Contact Me</span>
    </nav>
  </header>

  <div class="author-photo" role="img" aria-label="Sepia photo of the author standing on a city street in front of a bookshop window"></div>

  <section class="intro">
    <p>Lorem ipsum dolor sit amet, consectetuer adipiscing elit, sed diam nonummy nibh euismod tincidunt ut laoreet dolore magna aliquam erat volutpat. Ut wisi enim ad minim veniam, quis nostrud exerci tation ullamcorper suscipit lobortis nisl ut aliquip ex ea commodo consequat.</p>
    <p>Duis autem vel eum iriure dolor in hendrerit in vulputate velit esse molestie consequat, vel illum dolore eu feugiat nulla facilisis at vero eros et accumsan et iusto odio dignissim qui blandit praesent luptatum zzril delenit augue duis dolore te feugait nulla facilisi.</p>
    <p>Lorem ipsum dolor sit amet, cons ectetuer adipiscing elit, sed diam nonummy nibh euismod tincidunt ut laoreet dolore magna aliquam erat volutpat. Ut wisi enim ad minim veniam, quis nos</p>
  </section>

  <section class="memorial">
    <h1 class="memorial-title">
      <span class="memorial-title__lead">In my Loving<br>Memory of</span>
      <span class="memorial-title__name">Marlena</span>
    </h1>
    <div class="memorial-text">
      <p>Over the years, our daughters’ friends overlapped one another and two or three became like daughters to Velma and me. Some even became our friends as they grew into adulthood. One had a father who tried to committed suicide multiple times. After one attempt she asked him, “why?” He said, “I am glad you can’t understand why, only someone who can travel to that dark a place can understand why”. He was eventually successful.</p>
      <p>She shared that story with us on August 14th when our daughter Marlena found that dark place in herself and took her life. We found a suicide note, then her body, then everything went into a fog. An hour or so later, my wife and I stood on the front lawn after the police interviews and watched as the corner slide a covered corpse into the white SUV with darkened windows. We stood there as the rain began to fall, and the sky sobbed with us. As they closed the back of the coroner’s Wayfarer, the rain fell harder and harder and a fireman guided us back into the house that will never be the same for us.</p>
    </div>
  </section>

  <section class="newsletter">
    <h2 class="newsletter__title">SIGN UP FOR<svg class="newsletter__icon" viewBox="0 0 46 34"><g fill="none" stroke="#fff" stroke-width="2.5" stroke-linejoin="round"><path d="M8 3 L44 10 L38 32 L2 25 Z"/><path d="M8 3 L22 20 L44 10"/><path d="M2 25 L17 14"/><path d="M38 32 L28 17"/></g></svg><br>MY NEWSLETTER</h2>
    <form class="newsletter__form">
      <input class="newsletter__input" type="email" aria-label="Email address">
      <button class="newsletter__button" type="button">SIGN UP</button>
    </form>
  </section>

  <div class="owl-art" role="img" aria-label="Photo of a great horned owl"></div>

  <section class="recommendations">
    <h2 class="recommend-title">MY BOOK<svg class="recommend-title__icon" viewBox="0 0 42 42"><g fill="none" stroke="#ab4305" stroke-width="3" stroke-linejoin="round"><path d="M4 10 L18 14 L18 38 L4 34 Z"/><path d="M18 14 L34 4 L34 28 L18 38"/><path d="M22 18 L30 13 M22 24 L30 19 M22 30 L30 25"/><path d="M34 10 L38 10 L38 32 L20 40"/></g></svg><br>RECOMENDATIONS</h2>
    <div class="book book--one"><div class="book__cover" role="img" aria-label="Book cover"></div><div class="book__title">Prairie Lantern<br>Stories</div></div>
    <div class="book book--two"><div class="book__cover" role="img" aria-label="Book cover"></div><div class="book__title">Prairie Lantern<br>Stories</div></div>
    <div class="book book--three"><div class="book__cover" role="img" aria-label="Book cover"></div><div class="book__title">Prairie Lantern<br>Stories</div></div>
  </section>

  <footer class="footer">Copyright © 2018 - InkAndPlains.com</footer>
</body>
</html>
```